A new website for Electrical Contractor Business

We are looking for a unique and new WordPress website design which would include 5 Pages - Home Page, Meet the Team, Our Services, Our Projects and Contact Us page.

The global theme for the website needs to be professional but simple to navigate as we cater for both business and home owner customers.

Our core business service is targeted around lighting from single room decorative to large office so the theme should incorporate this in some way.

The home page should include;
Our business logo, Contact number, Email address, small Image rotation box - Highlighting pervious projectsText box - With welcome message, chirpnet feed news reel/Customer feed back box.

I would also like to see a 2 boxes for the separate customer types we services. Business and Home Owner. each box will have a small image with a small text description with a link to the area of the services page relevant to that customer type.

Meet the team page -This will be introducing potential customers to the team so I would like it to include for each team member. Something like a small image and text area which will introduce an outline of the team members skills and abilities.

Our Services page This page will be outlining the different services on offer to the both customer types business and homeowner. Each service should have an image with text description of the service would good here.

Our projects page-Will include images of pervious projects and work we have completed along with a text area for the project description/ outliner.

Contact Us page - Should include a contact form which should include an option for the customer to quest us to call them back, also a selection box for them to inform us our how they found our details would be good.

Colour - The theme colours can be taken from the logo or feel free to impress with your own imagination.

Remember we are looking for a website that will interest our customers enough to except our services or be drawn further into the website.. So call to action links to other areas of the site/ contact page are welcome

Target Market(s)

Business - Office, warehousing and Large Store - lighting and Power
Home owner lighting and power

Coding

Coded - Design and coding required

Number of Pages Required

5+ page

Font styles to use
Serif
Sans Serif

Colors

Designer to choose colors to be used in the design.

Requirements
Must have
• Logo integrated into the website design - i.e. website colours which allow the logo to blend into the design.
Nice to have
• Custom but professional theme catering to business customers, but also show that we do provide services to home owners too.
Should not have
• Sorry am not interested in one oversized block image on rotation covering half the home page.. Images will be needed but not a single block over sized frame with not text, shape. Please use your imagination when considering this design

```html
<!DOCTYPE html>
<html lang="en">
<head>
<meta charset="utf-8">
<title>Brightwire Electrical</title>
<link rel="stylesheet" href="https://fonts.googleapis.com/css2?family=Montserrat:wght@400;600;700&family=Open+Sans:wght@400;600&display=swap">
<style>
:root{
  --orange:#f26a21;
  --blue:#1d3f9a;
  --navy:#14296b;
  --ink:#222;
  --muted:#666;
  --line:#e3e3e3;
  --light:#f4f4f4;
  --black:#0b0b0b;
}
*{box-sizing:border-box;margin:0;padding:0}
html,body{width:1200px;height:2396px;overflow:hidden;background:#fff}
body{font-family:"Open Sans",Arial,sans-serif;color:var(--ink);font-size:12px;line-height:1.6}
h1,h2,h3,h4{font-family:"Montserrat",Arial,sans-serif}
.page{position:relative;width:1200px;height:2396px}

/* header */
.header{height:80px;position:relative;background:#fff;border-top:4px solid var(--orange)}
.topbar{width:740px;margin:0 auto;height:32px;display:flex;justify-content:space-between;align-items:center}
.social{display:flex;gap:6px}
.social span{width:14px;height:14px;border-radius:50%;background:var(--blue)}
.contact-top{display:flex;gap:22px;font-size:10px;color:var(--muted)}
.contact-top b{color:var(--orange);margin-right:4px}
.navrow{width:780px;margin:0 auto;display:grid;grid-template-columns:1fr auto 1fr;align-items:center;height:36px}
.nav{display:flex;gap:2px}
.nav.left{justify-content:flex-end}
.nav.right{justify-content:flex-start}
.nav a{font-family:"Montserrat",sans-serif;font-size:11px;font-weight:600;color:var(--ink);text-decoration:none;padding:8px 12px;white-space:nowrap}
.nav a.active{background:var(--blue);color:#fff}
.brand{padding:0 26px;font-family:"Montserrat",sans-serif;font-weight:700;font-size:15px;color:var(--navy);white-space:nowrap}

/* hero */
.hero{position:relative;height:260px;background:linear-gradient(100deg,#c9ccd0,#8b9096 45%,#3a3f46);text-align:center;color:#fff}
.hero .photo{position:absolute;inset:0}
.hero .copy{position:relative;padding-top:90px}
.hero h1{font-size:30px;font-weight:700}
.hero p{width:520px;margin:10px auto 16px;font-size:11px;opacity:.9}
.btn{display:inline-block;font-family:"Montserrat",sans-serif;font-size:10px;font-weight:600;padding:8px 18px;text-decoration:none}
.btn.blue{background:var(--blue);color:#fff}
.btn.orange{background:var(--orange);color:#fff}

/* emergency */
.emergency{height:260px;text-align:center;padding-top:40px}
.section-title{font-size:17px;font-weight:700;color:var(--ink);text-transform:uppercase}
.rule{width:60px;height:2px;background:var(--orange);margin:8px auto 18px}
.emergency p{width:820px;margin:0 auto 24px;color:var(--muted);font-size:11px}
.cta-row{display:flex;justify-content:center;align-items:center;gap:30px}
.phone{text-align:left;font-family:"Montserrat",sans-serif}
.phone small{display:block;font-size:9px;color:var(--muted)}
.phone strong{font-size:13px;color:var(--blue)}

/* services */
.services{height:470px;background:var(--light);padding-top:36px;text-align:center}
.cards{display:flex;justify-content:center;gap:26px}
.service-card{width:360px;background:#fff;border:2px solid var(--orange);text-align:center}
.service-card .photo{height:170px;background:linear-gradient(135deg,#d9cfc2,#9c8b78)}
.service-card.business .photo{background:linear-gradient(135deg,#c7ccd4,#6e7886)}
.service-card h3{font-size:15px;color:var(--blue);margin:14px 0 6px}
.service-card p{padding:0 26px;font-size:10px;color:var(--muted)}
.service-card .more{display:block;text-align:right;padding:10px 18px 12px;font-size:10px;color:var(--orange);font-weight:600}

/* testimonial */
.testimonial{height:330px;position:relative;background:var(--blue);color:#fff}
.testimonial .left{position:absolute;left:0;top:0;width:330px;height:100%;background:var(--orange)}
.testimonial .avatar{position:absolute;left:280px;top:110px;width:110px;height:110px;border-radius:50%;background:linear-gradient(135deg,#b9aa9a,#6f6256);border:4px solid #fff}
.testimonial .quote{position:absolute;left:440px;top:100px;width:440px}
.testimonial h2{font-size:15px;margin-bottom:10px}
.testimonial p{font-size:11px;opacity:.92}
.testimonial .who{display:block;margin-top:12px;color:var(--orange);font-weight:600;font-size:10px}

/* team */
.team{height:360px;padding-top:36px;text-align:center}
.team-grid{display:flex;justify-content:center;gap:30px}
.member{width:220px;border:1px solid var(--line);background:#fff}
.member .photo{height:170px;background:linear-gradient(160deg,#e9b847,#8a7a64)}
.member h4{font-size:10px;margin:10px 0 4px;color:var(--ink)}
.member p{font-size:9px;color:var(--muted);padding:0 14px}
.member .dots{display:flex;justify-content:center;gap:5px;padding:8px 0 10px}
.member .dots span{width:8px;height:8px;border-radius:50%;background:var(--blue)}

/* projects */
.projects{height:320px;text-align:center;padding-top:10px}
.tabs{display:flex;justify-content:center;gap:22px;font-size:10px;margin:-6px 0 14px;color:var(--muted)}
.tabs .on{color:var(--orange);font-weight:600}
.gallery{display:grid;grid-template-columns:repeat(5,104px);grid-auto-rows:86px;gap:4px;justify-content:center}
.gallery div{background:linear-gradient(135deg,#9aa4b2,#2f3a4d)}
.gallery div:nth-child(2n){background:linear-gradient(135deg,#d8c7a6,#7a6448)}
.gallery div:nth-child(3n){background:linear-gradient(135deg,#3b4e9a,#0f1a44)}

/* newsletter */
.newsletter{height:80px;background:var(--navy);display:flex;align-items:center;justify-content:center;gap:22px;color:#fff}
.newsletter h3{font-size:14px;font-weight:600}
.field{width:150px;height:28px;background:#fff;color:#999;font-size:10px;padding:6px 10px}

/* footer */
.footer{height:236px;background:var(--black);color:#aaa;position:relative;font-size:10px}
.footer .about{position:absolute;left:240px;top:36px;width:240px}
.footer .brand-f{font-family:"Montserrat",sans-serif;font-weight:700;color:#fff;font-size:13px;margin-bottom:14px}
.footer .links{position:absolute;left:580px;top:36px;list-style:none;line-height:2}
.footer .links li{color:#ccc}
.footer .contact{position:absolute;left:790px;top:36px;line-height:2}
.footer h4{color:#fff;font-size:11px;margin-bottom:4px}
.footer .contact b{color:var(--orange);margin-right:6px}
.footer .copy{position:absolute;bottom:14px;width:100%;text-align:center;font-size:9px;color:#777}
</style>
</head>
<body>
<div class="page">

<header class="header">
  <div class="topbar">
    <div class="social" aria-label="Social links"><span></span><span></span><span></span><span></span></div>
    <div class="contact-top"><div><b>✉</b>hello@brightwire.co</div><div><b>☎</b>0800 123 7890</div></div>
  </div>
  <div class="navrow">
    <nav class="nav left"><a class="active" href="#">Home</a><a href="#">About Us</a><a href="#">Meet Our Team</a></nav>
    <div class="brand">Brightwire</div>
    <nav class="nav right"><a href="#">Services</a><a href="#">Projects</a><a href="#">Contact Us</a></nav>
  </div>
</header>

<section class="hero">
  <div class="photo" role="img" aria-label="Electrician working on a switchboard panel"></div>
  <div class="copy">
    <h1>Electrician Services</h1>
    <p>Safe, certified electrical work for homes and businesses, from a single light fitting to full office and warehouse lighting installs.</p>
    <a class="btn blue" href="#">Learn More</a>
  </div>
</section>

<section class="emergency">
  <h2 class="section-title">Emergency Electrician</h2>
  <div class="rule"></div>
  <p>When power fails you need help fast. Our qualified electricians are on call day and night to find the fault, make your property safe and restore lighting and power with minimal disruption. We cover homes, shops, offices and warehouses across the region, and every job is tested and certified before we leave. Call us now or request a callback and a member of our team will be in touch within the hour to arrange a visit.</p>
  <div class="cta-row">
    <a class="btn blue" href="#">Call for Service</a>
    <div class="phone"><small>Call us anytime</small><strong>0800 123 7890</strong></div>
  </div>
</section>

<section class="services">
  <h2 class="section-title">Our Services</h2>
  <div class="rule"></div>
  <div class="cards">
    <article class="service-card home">
      <div class="photo" role="img" aria-label="Bright modern living room with decorative lighting"></div>
      <h3>SERVICE FOR HOME</h3>
      <p>From feature lighting in a single room to full rewires, we bring safe, stylish power and light to your home with tidy work and clear pricing from start to finish.</p>
      <a class="more">View More &rarr;</a>
    </article>
    <article class="service-card business">
      <div class="photo" role="img" aria-label="Office team in a well lit workspace"></div>
      <h3>SERVICE FOR BUSINESS</h3>
      <p>Offices, warehouses and large stores rely on us for efficient lighting, power distribution and maintenance planned around your working hours to keep you running.</p>
      <a class="more">View More &rarr;</a>
    </article>
  </div>
</section>

<section class="testimonial">
  <div class="left"></div>
  <div class="avatar" role="img" aria-label="Client portrait"></div>
  <div class="quote">
    <h2>WHAT OUR CLIENTS SAYS</h2>
    <p>Brightwire relit our whole warehouse over two weekends without a single day of lost trade. The team was punctual, tidy and explained every step. Our energy bills have dropped and the floor has never looked brighter. We would recommend them to anyone.</p>
    <span class="who">James Carter, Operations Manager</span>
  </div>
</section>

<section class="team">
  <h2 class="section-title">Our Team</h2>
  <div class="rule"></div>
  <div class="team-grid">
    <div class="member"><div class="photo" role="img" aria-label="Electrician in hard hat"></div><h4>CHRISTIAN MOORE</h4><p>Lead electrician with fifteen years in commercial lighting.</p><div class="dots"><span></span><span></span><span></span></div></div>
    <div class="member"><div class="photo" role="img" aria-label="Electrician in hard hat"></div><h4>DANIEL HAYES</h4><p>Domestic specialist for rewires, fittings and safety checks.</p><div class="dots"><span></span><span></span><span></span></div></div>
    <div class="member"><div class="photo" role="img" aria-label="Electrician in hard hat"></div><h4>OLIVER GRANT</h4><p>Power systems engineer for warehouses and large stores.</p><div class="dots"><span></span><span></span><span></span></div></div>
  </div>
</section>

<section class="projects">
  <h2 class="section-title">Pervious Projects</h2>
  <div class="rule"></div>
  <div class="tabs"><span class="on">All</span><span>Home</span><span>Business</span></div>
  <div class="gallery" role="img" aria-label="Gallery of completed lighting projects">
    <div></div><div></div><div></div><div></div><div></div>
    <div></div><div></div><div></div><div></div><div></div>
  </div>
</section>

<section class="newsletter">
  <h3>Stay up to date on new properties and Industry News!</h3>
  <div class="field">Your Name</div>
  <div class="field">Your Email</div>
  <a class="btn orange" href="#">Subscribe</a>
</section>

<footer class="footer">
  <div class="about">
    <div class="brand-f">Brightwire</div>
    <p>Trusted local electricians delivering lighting and power for homes and businesses, fully certified and insured.</p>
  </div>
  <ul class="links">
    <li>Sitemap</li><li>Home</li><li>About Us</li><li>Meet Our Team</li><li>Our Services</li><li>Projects</li><li>chirpnet</li>
  </ul>
  <div class="contact">
    <h4>Contact Us</h4>
    <div><b>⌖</b>14 Ashford Road, Millbrook MB2 7QT</div>
    <div><b>☎</b>0800 123 7890</div>
    <div><b>✉</b>hello@brightwire.co</div>
  </div>
  <div class="copy">© Brightwire Electrical. All rights reserved.</div>
</footer>

</div>
</body>
</html>
```